Business Card for a finance professional

I need a business card design to introduce myself to a professional networking (mainly banks) and potential companies to hire and remember me. I would like to use black, grey, white and maybe gold/silver colors and maybe something with my initials(R L F P T). The final design should communicate seriousness, profissionalism and something innovative.

The basic informations in the card are: Name, e-mail, phone number and trabnet. (I'm thinking to put some directly short link to my trabnet account or maybe some app - non QR Code - to add my contacts to a phone directly.)

My name is Mariana Lopes Ferreira Pinto dos Reis (I prefer to use only 'Mariana Lopes' or 'Mariana Reis' but i'm open to other suggestions) and I have 26 years old (just if it helps to build based in my age).
Updates

Dear designers, I wish to thank your participation in this project! It was very difficult to choose one! Thank your for your work! Best regards and success. Mariana

Target Market(s)

Potential hires and big companies.

Industry/Entity Type

Finance

Requirements
Must have
• The informations required at the business card are:
Name: Mariana Lopes F. P. dos Reis
Email: mariana.lop.reis@quellomail.com
Phone: +55 61 8493 5710
TrabNet: http://br.trabnet-perfis.com/in/marianalr/
Nice to have
• Modern and innovative look.
I suggest to use the colors black, grey, white, gold and/or silver, but I'm open to other colors.
Should not have
• A message showing that I need to be hired. It's more to "know me and remember me" than "hire me please".

```html
<!DOCTYPE html>
<html lang="pt">
<head>
<meta charset="utf-8">
<title>Mariana Lopes — Cartão de visita</title>
<link rel="stylesheet" href="https://fonts.googleapis.com/css2?family=Lobster&family=Open+Sans:wght@400&family=Ubuntu:wght@300;400&display=swap">
<style>
  :root {
    --backdrop: #a8a8a8;
    --ink: #0a0c12;
    --gold-light: #f6c443;
    --gold-mid: #e9a52c;
    --gold-deep: #bd6717;
    --amber-text: #f0a534;
    --tab-top: #55575a;
    --tab-bottom: #141519;
    --tab-edge: #8a8c90;
    --contact-ink: #2a2116;
  }
  * { box-sizing: border-box; margin: 0; padding: 0; }
  html, body {
    width: 1200px; height: 960px; overflow: hidden;
    background: var(--backdrop);
  }
  .card {
    position: absolute; left: 284px; width: 610px; height: 381px;
    background: var(--ink);
    box-shadow: 0 3px 8px rgba(0,0,0,.35);
    overflow: hidden;
  }
  .card--front { top: 116px; }
  .card--back { top: 542px; }
  .gold-band {
    position: absolute; left: 0; width: 100%;
    background: radial-gradient(ellipse 60% 160% at 50% 50%, var(--gold-light) 0%, var(--gold-mid) 55%, var(--gold-deep) 100%);
  }
  .gold-band--top { top: 0; height: 67px; }
  .gold-band--bottom { bottom: 0; height: 77px; }
  .emblem-tab {
    position: absolute; left: 201px; top: 44px; width: 212px; height: 196px;
  }
  .monogram {
    position: absolute; left: 217px; width: 180px; top: 126px;
    text-align: center; color: var(--amber-text);
    font: 400 26px/32px "Ubuntu", sans-serif; letter-spacing: 6px;
    padding-left: 6px;
  }
  .full-name {
    position: absolute; left: 0; width: 100%; top: 244px;
    text-align: center; color: var(--amber-text);
    font: 400 29px/40px "Lobster", cursive;
    letter-spacing: 1px;
    text-shadow: 0 1px 2px rgba(0,0,0,.6);
  }
  .contact {
    position: absolute; color: var(--contact-ink);
    font: 400 14px/24px "Open Sans", sans-serif;
  }
  .contact--left { left: 37px; top: 320px; }
  .contact--right { right: 12px; top: 320px; }
  .tab-name {
    position: absolute; left: 201px; width: 212px; top: 100px;
    text-align: center; color: var(--amber-text);
    font: 300 38px/38px "Ubuntu", sans-serif;
  }
</style>
</head>
<body>

<section class="card card--front">
  <div class="gold-band gold-band--top"></div>
  <div class="gold-band gold-band--bottom"></div>
  <svg class="emblem-tab" viewBox="0 0 212 196" aria-hidden="true">
    <defs>
      <linearGradient id="tabFill" x1="0" y1="0" x2="0" y2="1">
        <stop offset="0" stop-color="var(--tab-top)"/>
        <stop offset="1" stop-color="var(--tab-bottom)"/>
      </linearGradient>
    </defs>
    <path d="M0 23 Q4 12 16 12 L196 12 Q208 12 212 23 Z" fill="#1b1c20"/>
    <path d="M16 4 L196 4 L196 149 L106 190 L16 149 Z" fill="url(#tabFill)" stroke="var(--tab-edge)" stroke-width="1"/>
  </svg>
  <p class="monogram">R L F P T</p>
  <p class="full-name">Mariana Lopes F. P. dos Reis</p>
  <p class="contact contact--left">mariana.lop.reis@quellomail.com<br>phone: +55 61 8493 5710</p>
  <p class="contact contact--right">http://br.trabnet-perfis.com/in/marianalr/</p>
</section>

<section class="card card--back">
  <div class="gold-band gold-band--top"></div>
  <div class="gold-band gold-band--bottom"></div>
  <svg class="emblem-tab" viewBox="0 0 212 196" aria-hidden="true">
    <defs>
      <linearGradient id="tabFillBack" x1="0" y1="0" x2="0" y2="1">
        <stop offset="0" stop-color="var(--tab-top)"/>
        <stop offset="1" stop-color="var(--tab-bottom)"/>
      </linearGradient>
    </defs>
    <path d="M0 23 Q4 12 16 12 L196 12 Q208 12 212 23 Z" fill="#1b1c20"/>
    <path d="M16 4 L196 4 L196 149 L106 190 L16 149 Z" fill="url(#tabFillBack)" stroke="var(--tab-edge)" stroke-width="1"/>
  </svg>
  <p class="tab-name">Mariana<br>Lopes</p>
</section>

</body>
</html>
```